Beauty Salon Industry - Web Design Project

zTrellis is a well-funded start up developing an Online Marketing Platform for small businesses in Europe.
We require a large number of high quality business web designs for our business website builder. Our business websites are seamlessly integrated into our Online Marketing systems and therefore it is important for designers to comply with our Design Guidelines.
This is our second contest and it will focus on the beauty salon industry. We will be running contents every 2-3 weeks for a new industry. Last month, we ran a contest for Builder website designs with 3 top prizes (plus £10 per variation) and we also paid out £25 per design for 20+ entries from designers who did not win the top prizes. So we encourage all entries!
We have included a wire frame this time to encourage you to be as creative as possible with your designs and layout while respecting the following guidelines:
1) You CAN change the layout as much as you like. If you think a vertical menu would look better, then use it. If you think the design would benefit from moving an element to a different location, then you can do that too.
2) You must include ALL the elements in the wire frame in your design.(e.g. latest 2 news entries, a testimonial, 1 gallery image, carousel etc...). Please make sure you have looked through the wire frame and know what is required. Entries that do not include all the elements will not qualify to win.
3) So remember, you CAN change the layout as much as you like but DO NOT remove any elements nor move them to a different page.
4) You may change the size and style of the carousel image. We would like to see as many variations of this as possible.
We are rewarding 3 prizes, and would like the winning designer to design the internal pages to the new design.
As always, if we think your designs could be incorporated into our system, but you do not win the competition, we will reward £25. Therefore, we encourage designers to submit as many designs as possible as we may award up to 25 designs.
Judging criteria : -
1) Visual Design
2) Layout must adhere to best practices and wireframe. If you decide to move elements around significantly please provide reason
3) Functional, informative and drives calls to action
Updates
As usual:
1st place = £350
2nd place = £250
3rd place = £150
Good luck!
Very happy with all the designs submitted so far, and will provide feedback ASAP.
We would like to see you try arranging the elements differently. So please try different navigation types and layouts.
Thanks
Morris
Prize funds for 1st place has been slightly increased.
Thanks
Morris
We have already had some amazing designs submitted. Thanks.
Remember to play with the layout of the elements and try designs with a carousel/slider that is in portrait not just in landscape.
Thanks everyone!
Morris
Hi everyone, we are really enjoying looking through the designs.
We have one NEW requirement. If you have used an image from http://www.quarnex-demo.net/ in your design, could you please replace it with another.
We are not associated with them.
Thank you.
I have just sent a poll around the office to vote on all the designs and hope to have the results soon.
Good luck and I hope to see all your great designs for our next project in a couple of weeks.
Morris
Hi everyone, we hope you have had a good holiday season. We will be rewarding the prizes very soon, hopefully today or tomorrow.
Thanks
Morris
We are currently going through all the designs that did not win our competition and will be contacting the designers of the designs we would like to use in our system, so please keep an eye on your inbox over the next few days.
Thank you
Morris
Target Market(s)
Beauty Salon Industry
Industry/Entity Type
Beauty Salon
Look and feel
Each slider illustrates characteristics of the customer's brand and the style your logo design should communicate.

```html
<!DOCTYPE html>
<html lang="en">
<head>
<meta charset="utf-8">
<title>Velora – Hair and Urban Spa</title>
<link href="https://fonts.googleapis.com/css2?family=PT+Sans:wght@400;700&family=Open+Sans:wght@400;600;700&family=Questrial&family=Roboto+Slab:wght@400&display=swap" rel="stylesheet">
<style>
:root{
  --red:#b0182a;
  --red-deep:#8c1022;
  --btn:#8a1426;
  --ink:#1c1c1c;
  --rule:#c9c9c9;
  --nav:#1d1d1d;
  --gold:#f4d21f;
  --band:#9b0f2e;
  --band-dark:#6d0a20;
  --foot:#282828;
  --panel:#efefef;
  --white:#fff;
}
*{box-sizing:border-box;margin:0;padding:0}
html,body{width:1090px;height:1200px;overflow:hidden;background:var(--white)}
body{font-family:"PT Sans",Arial,sans-serif;color:var(--ink);position:relative}
.abs{position:absolute}
.btn{position:absolute;display:flex;align-items:center;justify-content:center;background:linear-gradient(#a31a2f,var(--btn));color:var(--white);border-radius:4px;font-size:14px;box-shadow:0 1px 2px rgba(0,0,0,.35);white-space:nowrap}

/* header */
.site-header{position:absolute;left:0;top:0;width:1090px;height:141px;background:linear-gradient(#fff,#f3f3f3);border-top:4px solid #e6e6e6}
.brand-dot{position:absolute;left:29px;top:29px;width:89px;height:89px;border-radius:50%;background:var(--red)}
.brand-name{position:absolute;left:133px;top:30px;font-size:50px;color:var(--red);font-weight:400;letter-spacing:-1px}
.brand-tag{position:absolute;left:134px;top:88px;font-size:19px;color:#444}
.phone{position:absolute;right:23px;top:28px;font-family:"Questrial",sans-serif;font-size:35px;color:#333;letter-spacing:1px}
.buy-now{position:absolute;left:921px;top:81px;width:142px;height:44px;background:linear-gradient(#3a3a3a,#0d0d0d);border:2px solid #666;border-radius:4px;color:#fff;font-family:"Open Sans",sans-serif;font-weight:700;font-size:20px;display:flex;align-items:center;justify-content:center;gap:8px}

/* nav */
.main-nav{position:absolute;left:0;top:141px;width:1090px;height:51px;background:linear-gradient(#3b3b3b,var(--nav) 60%,#111)}
.main-nav a{position:absolute;top:15px;font-size:16px;color:#e8e8e8;text-decoration:none}
.main-nav a.active{color:var(--gold)}
.nav-dot{position:absolute;top:24px;width:7px;height:7px;border-radius:50%;background:#8a8a8a}
.nav-sep{position:absolute;left:801px;top:12px;width:1px;height:27px;background:#555}
.search{position:absolute;left:821px;top:13px;width:196px;height:25px;background:#fff;border-radius:4px;font-size:12px;color:#aaa;padding:5px 14px}
.go{position:absolute;left:1027px;top:14px;width:43px;height:23px;border-radius:10px;background:var(--red);color:#fff;font-weight:700;font-size:15px;text-align:center;line-height:22px}

/* intro column */
.intro-title{left:11px;top:222px;width:236px;font-size:23px;line-height:25px;color:var(--red);font-weight:400;white-space:nowrap}
.intro-text{left:10px;width:226px;font-size:14.5px;line-height:20.6px}
.intro-rule{left:10px;top:406px;width:221px;height:3px;background:#d8d8d8}
.gallery-card{left:6px;top:595px;width:226px;height:250px;border-radius:8px;overflow:hidden;background:linear-gradient(160deg,#c9a89a,#6b4636 55%,#1e1512)}
.gallery-bar{position:absolute;left:0;bottom:0;width:100%;height:34px;background:rgba(20,20,20,.88);color:#fff;font-size:17px;padding:6px 12px;display:flex;justify-content:space-between}
.gallery-bar em{font-style:normal;color:#e5327a}
.gallery-bar .more{color:#4aa0ff;text-decoration:underline;font-size:15px;padding-top:2px}

/* slider */
.slider{left:252px;top:203px;width:563px;height:387px;border-radius:8px;overflow:hidden;border:1px solid #555;background:radial-gradient(circle at 70% 30%,#d2232e,#a0111c 55%,#5a0810)}
.slider-photo{position:absolute;left:0;top:0;width:225px;height:387px;background:linear-gradient(90deg,#7a3c27,#c98e72 50%,#2a1a16)}
.offer{position:absolute;left:250px;top:92px;color:#fff;font-size:22px}
.product{position:absolute;left:249px;top:112px;color:#fff;font-family:"Open Sans",sans-serif;font-size:34px;font-weight:700;letter-spacing:2px;text-shadow:0 2px 3px rgba(0,0,0,.4);line-height:44px}
.slide-copy{position:absolute;left:255px;top:162px;width:292px;color:#fff;font-size:14.5px;line-height:23px}
.more-info{position:absolute;left:255px;top:266px;width:127px;height:27px;background:linear-gradient(#fff,#d6d6d6);color:#333;border-radius:3px;font-size:14px;display:flex;align-items:center;justify-content:center}
.arrow{position:absolute;top:185px;color:#fff;font-size:32px;line-height:1}
.pager{position:absolute;left:467px;top:350px;width:86px;height:24px;border-radius:12px;background:rgba(0,0,0,.45);display:flex;gap:3px;align-items:center;justify-content:center}
.pager span{width:11px;height:11px;background:#222}
.pager span.on{background:#fff}

/* testimonial */
.quote{left:259px;top:600px;width:556px;font-family:"Roboto Slab",serif;font-size:14.6px;line-height:19px}
.quote-name{left:259px;top:651px;width:113px;height:27px;border:1px solid #ccc;border-radius:8px;background:linear-gradient(#fff,#eee);color:var(--red);font-size:13px;font-weight:700;display:flex;align-items:center;justify-content:center}

/* news */
.news-panel{left:252px;top:697px;width:566px;height:171px;background:var(--panel)}
.news-card{position:absolute;top:16px;width:265px;height:135px;background:#fff;padding:16px 14px}
.news-card h3{font-size:17px;color:var(--red-deep);font-weight:700;margin-bottom:6px}
.news-card p{font-size:13.5px;line-height:16.5px}
.news-card time{display:block;margin-top:8px;font-size:13.5px;color:var(--red)}

/* aside */
.promo{left:830px;top:217px;width:254px;height:299px;border-radius:6px;overflow:hidden;background:linear-gradient(#111,#2b2b2b 60%,#1a1a1a)}
.promo-photo{position:absolute;left:88px;top:45px;width:122px;height:95px;border-radius:6px;background:linear-gradient(120deg,#e04aa0,#7fd3e0)}
.free{position:absolute;left:10px;top:16px;color:var(--gold);font-weight:700;font-size:15px;line-height:1.2}
.free b{font-size:32px;display:block}
.scent{position:absolute;right:14px;top:20px;color:#fff;font-size:16px;font-style:italic}
.promo-text{position:absolute;left:0;top:162px;width:100%;text-align:center;color:#fff;font-size:21px;font-weight:700;line-height:23px}
.book{left:13px;top:236px;width:224px;height:42px;font-size:18px;font-weight:700}
.aside-title{left:834px;font-size:23px;font-weight:400;color:var(--red);white-space:nowrap}
.aside-rule{left:834px;width:221px;height:2px;background:var(--rule)}
.aside-text{left:837px;font-size:14.5px;line-height:25px}
.hours{left:837px;top:735px;font-size:14.5px;line-height:20.6px;list-style:none}

/* brands */
.brands{left:0;top:895px;width:1090px;height:206px;background:linear-gradient(#b01238,var(--band) 40%,var(--band-dark))}
.brand-tile{position:absolute;top:26px;width:226px;height:151px;border-radius:6px}
.round-arrow{position:absolute;top:82px;width:32px;height:32px;border-radius:50%;background:#2a2a2a;border:2px solid #555;color:#fff;font-size:14px;font-weight:700;display:flex;align-items:center;justify-content:center}

/* footer */
.site-footer{left:0;top:1101px;width:1090px;height:99px;background:var(--foot);color:#fff}
.foot-links{position:absolute;left:16px;top:34px;font-size:14.5px;font-weight:700;display:flex;gap:9px}
.copy{position:absolute;left:16px;top:58px;font-size:13px;color:#ddd}
.managed{position:absolute;left:843px;top:48px;font-size:13px}
.managed b{font-size:14.5px}
.admin{position:absolute;left:1016px;top:46px;color:var(--gold);font-weight:700;font-size:14.5px}
</style>
</head>
<body>

<header class="site-header">
  <div class="brand-dot"></div>
  <div class="brand-name">Velora</div>
  <div class="brand-tag">Hair and Urban Spa</div>
  <div class="phone">020 7946 0418</div>
  <div class="buy-now">BUY NOW
    <svg width="16" height="16" viewBox="0 0 16 16"><path d="M1 8h11M8 3l5 5-5 5" stroke="#fff" stroke-width="3" fill="none"/></svg>
  </div>
</header>

<nav class="main-nav">
  <a class="active" style="left:28px">Home</a>
  <span class="nav-dot" style="left:95px"></span>
  <a style="left:133px">Services</a>
  <span class="nav-dot" style="left:214px"></span>
  <a style="left:244px">Gallery</a>
  <span class="nav-dot" style="left:317px"></span>
  <a style="left:349px">Testimonials</a>
  <span class="nav-dot" style="left:458px"></span>
  <a style="left:491px">News</a>
  <span class="nav-dot" style="left:559px"></span>
  <a style="left:593px">About Us</a>
  <span class="nav-dot" style="left:672px"></span>
  <a style="left:702px">Contact Us</a>
  <span class="nav-sep"></span>
  <div class="search">search</div>
  <div class="go">go!</div>
</nav>

<h2 class="abs intro-title">Let our Hair and Beauty<br>Skills Blow you away</h2>
<p class="abs intro-text" style="top:284px">Velora is a passionate, creative team, dedicated to delivering a second to none, personal salon experience that will ‘blow’ your mind.</p>
<div class="abs intro-rule"></div>
<p class="abs intro-text" style="top:428px">Where ultimate hairdressing comes hand-in-hand with style, glamour, fashion, innovation and skill to create an exquisitesalon experience in the heart of London.</p>
<div class="btn" style="left:8px;top:546px;width:82px;height:28px">read more</div>

<div class="abs gallery-card" role="img" aria-label="Portrait photo of a woman with auburn hair">
  <div class="gallery-bar"><span>Inspiration <em>Gallery</em></span><span class="more">more...</span></div>
</div>

<section class="abs slider">
  <div class="slider-photo" role="img" aria-label="Photo of a model with long hair in a black dress"></div>
  <div class="offer">10%-20% OFF</div>
  <div class="product">TINTORA</div>
  <p class="slide-copy">Lorem Ipsum is simply dummy text of the printing and typesetting industry. Lorem Ipsum has been the industry's standard dummy text ever since the 1500s...</p>
  <div class="more-info">more information</div>
  <span class="arrow" style="left:18px;opacity:.6">«</span>
  <span class="arrow" style="left:536px">»</span>
  <div class="pager"><span class="on"></span><span></span><span></span><span></span></div>
</section>

<p class="abs quote">My Hairstylist, Annika, was truly amazing. She listened to exactly what I wanted, but also told me exactly what...</p>
<div class="abs quote-name">Mirela Oakes</div>
<div class="btn" style="left:665px;top:649px;width:149px;height:28px">read more testimonials</div>

<section class="abs news-panel">
  <article class="news-card" style="left:14px">
    <h3>Book Now for Christmas</h3>
    <p>Our Salon is usually very busy for the two weeks before christmas, so please book early: call 020 7946 0418, or contact us.</p>
    <time>1 Dec. 2011</time>
  </article>
  <article class="news-card" style="left:289px">
    <h3>Want to be a hair model?</h3>
    <p>We always need models for our portfolio. If you want to become one please contact us.</p>
    <time>9 Nov. 2011</time>
  </article>
  <div class="btn" style="left:460px;top:134px;width:82px;height:27px">more news</div>
</section>

<aside class="abs promo">
  <div class="promo-photo" role="img" aria-label="Photo of two perfume bottles"></div>
  <div class="free">FREE GIFT<b>£25</b></div>
  <div class="scent">Aurel Scents</div>
  <div class="promo-text">Complimentary gift<br>for first-time clients!</div>
  <div class="btn book">Book Appointment Now</div>
</aside>

<h3 class="abs aside-title" style="top:528px">Velora Address:</h3>
<div class="abs aside-rule" style="top:563px"></div>
<p class="abs aside-text" style="top:579px">12 Linden Row<br>London - W2C 4QT</p>
<div class="btn" style="left:988px;top:632px;width:74px;height:25px;font-size:13px">View Map</div>
<div class="abs aside-rule" style="top:686px"></div>
<h3 class="abs aside-title" style="top:692px">Business Hours</h3>
<div class="abs aside-rule" style="top:726px"></div>
<ul class="abs hours">
  <li>Mon, 9 a.m - 5 p.m</li>
  <li>Tue. 9 a.m - 5 p.m</li>
  <li>Wed. 9 a.m - 5 p.m</li>
  <li>Thu. 9 a.m - 5 p.m</li>
  <li>Fri. 9 a.m - 5 p.m</li>
  <li>Sat. 9 a.m - 5 p.m</li>
</ul>

<section class="abs brands">
  <div class="round-arrow" style="left:5px">«</div>
  <div class="brand-tile" style="left:52px;background:linear-gradient(100deg,#e9d6cc,#f3f3f5 60%,#7fb3d6)" role="img" aria-label="Skincare advertisement with a model"></div>
  <div class="brand-tile" style="left:305px;background:linear-gradient(120deg,#f2e6e0,#c8642c 50%,#8a3516)" role="img" aria-label="Hair care advertisement with copper hair"></div>
  <div class="brand-tile" style="left:560px;background:linear-gradient(90deg,#f4f4f4,#d0d0d0 45%,#3a3a3a)" role="img" aria-label="Styling products advertisement"></div>
  <div class="brand-tile" style="left:811px;background:linear-gradient(110deg,#3a2b26,#a97763 45%,#d9c4bb)" role="img" aria-label="Hair colour advertisement with a model"></div>
  <div class="round-arrow" style="left:1049px">»</div>
</section>

<footer class="abs site-footer">
  <div class="foot-links"><span>Home</span><span>Services</span><span>Gallery</span><span>Testimonials</span><span>News</span><span>About Us</span><span>Contact Us</span></div>
  <div class="copy">All rights reserved 2011</div>
  <div class="managed">Managed by <b>zTrellis.com</b></div>
  <div class="admin">Admin</div>
</footer>

</body>
</html>
```